Maple Sprout Menu (Vegetarian Restaurant Concept)

Maple Sprout is a new concept fast casual restaurant
renders are attached so you can see the style of restaurant
Maple Sprowt is a vibrant and modern Vegetarian fast casual restaurant concept that mixes fresh food, energy, great décor, and a comfortable, welcoming atmosphere to provide a memorable and all Vegetarian dining experience.
Our Mission is to be top of mind when consumers think Vegetarian food!
Target Market(s)
the menu is vegetarian and appeals to a broad demographic in USA
Colors
Designer to choose colors to be used in the design.
Requirements
Must have
- well colored and well laid out menu - should not be cartoonish
Nice to have
- For Phots please use the shots in this file:
- https://www.filecrate-example.net/sh/kq7trm2wzl4pnad/BBBxT_qPwLdRNVoE_KMS_Tb?dl=0
- note these are untouched and you are free to change as needed
Should not have
- Should not be cartoonish - nor kives, forks etc in the design

```html
<!DOCTYPE html>
<html lang="en">
<head>
<meta charset="utf-8">
<title>Maple Sprowt — Menu</title>
<link rel="stylesheet" href="https://fonts.googleapis.com/css2?family=Nunito+Sans:wght@400;600;700;800&family=Ubuntu:wght@500&family=Cinzel:wght@400&family=Kaushan+Script&display=swap">
<style>
  :root {
    --stage: #262626;
    --paper-light: #ebeae8;
    --paper-light-2: #dcdbd8;
    --wood-grey: #7a7a7a;
    --wood-grey-2: #666666;
    --white: #ffffff;
    --ink: #2b2b2b;
    --leaf: #5a9a2e;
    --leaf-light: #6fae3c;
    --leaf-dark: #4f8c27;
    --badge: #6aa78b;
    --slate: #3a3a3a;
    --slate-2: #2c2c2c;
    --rule: rgba(255,255,255,0.55);
  }
  * { box-sizing: border-box; margin: 0; padding: 0; }
  html, body { width: 1200px; height: 1200px; overflow: hidden; background: var(--stage); }
  body { position: relative; font-family: "Nunito Sans", sans-serif; }

  .page { position: absolute; top: 54px; width: 538px; height: 724px; overflow: hidden; }
  .page--cover { left: 46px; background: linear-gradient(90deg, var(--paper-light), var(--paper-light-2) 50%, var(--paper-light)); }
  .page--inside { left: 615px; background: var(--slate); }

  /* Cover */
  .cover__texture { position: absolute; top: 0; height: 100%; width: 145px;
    background: linear-gradient(180deg, #eeedeb, #e2e1de); }
  .cover__texture--left { left: 0; }
  .cover__texture--right { right: 0; width: 148px; }
  .cover__column { position: absolute; left: 145px; width: 245px; top: 0; height: 100%; }
  .cover__brand { position: absolute; left: 0; top: 0; width: 100%; height: 322px; background: var(--white);
    display: flex; flex-direction: column; align-items: center; justify-content: center; gap: 34px; padding-top: 20px; }
  .brand__dot { width: 62px; height: 62px; border-radius: 50%; background: var(--leaf); }
  .brand__name { font-family: "Ubuntu", sans-serif; font-weight: 500; font-size: 31px; color: var(--ink);
    white-space: nowrap; text-align: center; letter-spacing: 0.3px; }
  .cover__panel { position: absolute; left: 0; top: 322px; width: 100%; height: 402px;
    background: linear-gradient(90deg, var(--wood-grey-2), var(--wood-grey) 50%, var(--wood-grey-2)); }
  .badge { position: absolute; left: 166px; top: 422px; width: 208px; height: 208px; border-radius: 50%;
    background: var(--badge); display: flex; flex-direction: column; align-items: center; justify-content: center;
    color: var(--white); padding-top: 8px; }
  .badge__script { font-family: "Kaushan Script", cursive; font-size: 36px; line-height: 1; }
  .badge__sub { display: flex; align-items: center; gap: 6px; font-family: "Kaushan Script", cursive; font-size: 17px; line-height: 1; margin-top: -2px; }
  .badge__sub::before, .badge__sub::after { content: ""; width: 38px; height: 2px; background: var(--white); }
  .badge__label { font-family: "Cinzel", serif; font-size: 15px; letter-spacing: 2px; margin-top: 12px; }

  /* Inside */
  .inside__green { position: absolute; left: 0; top: 0; width: 269px; height: 100%;
    background: repeating-linear-gradient(180deg, var(--leaf) 0 40px, var(--leaf-dark) 40px 82px); }
  .inside__slate { position: absolute; left: 269px; top: 0; width: 269px; height: 414px;
    background: linear-gradient(90deg, var(--slate-2), var(--slate) 40%, var(--slate-2)); }
  .inside__produce { position: absolute; left: 269px; top: 414px; width: 269px; height: 310px;
    background: radial-gradient(ellipse at 40% 20%, #e8c94a 0 18%, transparent 32%),
                radial-gradient(ellipse at 90% 15%, #5ea734 0 14%, transparent 26%),
                radial-gradient(ellipse at 35% 65%, #4b2440 0 26%, transparent 44%),
                radial-gradient(ellipse at 70% 80%, #c9352a 0 14%, transparent 26%),
                linear-gradient(160deg, #9e2a22, #2e2a26 55%, #3d6b26); }

  .section-head { position: absolute; left: 25px; width: 513px; height: 42px; display: flex; align-items: center; }
  .section-head::before { content: ""; position: absolute; left: 0; top: 0; width: 244px; height: 100%; background: var(--leaf-light); opacity: 0.85; }
  .section-head__title { position: relative; font-weight: 700; font-size: 16px; color: var(--white); padding-left: 9px; }
  .section-head__rule { position: relative; flex: 1; height: 1px; background: var(--rule); margin: 0 17px 0 14px; }
  .section-head--salads { top: 16px; }
  .section-head--toasts { top: 426px; }
  .section-head--toasts .section-head__rule { margin-right: 300px; }

  .dish { position: absolute; left: 20px; width: 410px; color: var(--white); }
  .dish__row { display: flex; align-items: baseline; }
  .dish__bullet { width: 6px; height: 6px; border-radius: 50%; background: var(--white); margin-right: 5px; flex: none; transform: translateY(-1px); }
  .dish__name { font-weight: 800; font-size: 11.5px; white-space: nowrap; }
  .dish__leader { flex: 1; border-bottom: 1px dotted var(--rule); margin: 0 4px 0 3px; }
  .dish__qty, .dish__price { font-weight: 800; font-size: 8px; letter-spacing: 0.3px; }
  .dish__price { margin-left: 12px; width: 22px; }
  .dish__desc { margin-left: 11px; margin-top: 2px; font-size: 9.5px; line-height: 13.5px; font-weight: 400; }

  .thumb { position: absolute; left: 439px; width: 82px; height: 70px; border-radius: 8px; background: var(--white);
    display: flex; align-items: center; justify-content: center; }
  .thumb__photo { width: 60px; height: 60px; border-radius: 50%; }
  .thumb__photo--greens { background: radial-gradient(circle, #4f8a2e, #2f5a1c 60%, #e5dccb 62%); }
  .thumb__photo--beet { background: radial-gradient(circle, #6b2b3a, #3f6a26 60%, #e5dccb 62%); }
  .thumb__photo--cups { background: radial-gradient(circle, #b7d67a, #6fae3c 60%, #e5dccb 62%); }
  .thumb__photo--mixed { background: radial-gradient(circle, #8a3a2a, #3f6a26 60%, #e5dccb 62%); }
  .thumb__photo--avocado { background: radial-gradient(circle, #d9a43a, #c65a2a 55%, #e5dccb 62%); }
  .thumb__photo--bruschetta { background: radial-gradient(circle, #7a1f2c, #5c2a2a 55%, #e5dccb 62%); }
  .thumb__photo--melt { background: radial-gradient(circle, #e0b04a, #c87a3a 55%, #e5dccb 62%); }
</style>
</head>
<body>
  <section class="page page--cover">
    <div class="cover__texture cover__texture--left" role="img" aria-label="Light wood planks with hand-drawn vegetable sketches"></div>
    <div class="cover__texture cover__texture--right" role="img" aria-label="Light wood planks with hand-drawn vegetable sketches"></div>
    <div class="cover__column">
      <div class="cover__brand">
        <span class="brand__dot"></span>
        <span class="brand__name">Maple Sprowt</span>
      </div>
      <div class="cover__panel" role="img" aria-label="Grey wood plank texture"></div>
    </div>
    <div class="badge">
      <span class="badge__script">healthy</span>
      <span class="badge__sub">food</span>
      <span class="badge__label">MENU</span>
    </div>
  </section>

  <section class="page page--inside">
    <div class="inside__green" role="img" aria-label="Green panel with faint vegetable sketches"></div>
    <div class="inside__slate" role="img" aria-label="Dark wood texture"></div>
    <div class="inside__produce" role="img" aria-label="Photo of fresh corn, chillies, red onions, tomatoes and lettuce"></div>

    <div class="section-head section-head--salads"><span class="section-head__title">Salads</span><span class="section-head__rule"></span></div>

    <div class="dish" style="top: 88px;">
      <div class="dish__row"><span class="dish__bullet"></span><span class="dish__name">Brussel Sprout Ceasar</span><span class="dish__leader"></span><span class="dish__qty">QUANTITY</span><span class="dish__price">USD</span></div>
      <p class="dish__desc">little gem romaine, toasted torn bread,<br>parmigiano reggiano</p>
    </div>
    <div class="dish" style="top: 170px;">
      <div class="dish__row"><span class="dish__bullet"></span><span class="dish__name">Heirloom Beet salad</span><span class="dish__leader"></span><span class="dish__qty">QUANTITY</span><span class="dish__price">USD</span></div>
      <p class="dish__desc">shaved chioggia beet, roasted golden beet,<br>red quinoa, little gem, arugula,lemon vinaigrette</p>
    </div>
    <div class="dish" style="top: 265px;">
      <div class="dish__row"><span class="dish__bullet"></span><span class="dish__name">Zesty Black Bean &amp; Corn Salad in lettuce cups</span><span class="dish__leader"></span><span class="dish__qty">QUANTITY</span><span class="dish__price">USD</span></div>
      <p class="dish__desc">Black beans, avocado and roasted corn<br>topped with feta crumbles in butter lettuce</p>
    </div>
    <div class="dish" style="top: 347px;">
      <div class="dish__row"><span class="dish__bullet"></span><span class="dish__name">Green, Red and White</span><span class="dish__leader"></span><span class="dish__qty">QUANTITY</span><span class="dish__price">USD</span></div>
      <p class="dish__desc">Spring leaves, cherry tomatoes, avocado,<br>roasted almond and goat cheese</p>
    </div>

    <div class="thumb" style="top: 71px;"><span class="thumb__photo thumb__photo--greens" role="img" aria-label="Bowl of Brussel sprout caesar salad"></span></div>
    <div class="thumb" style="top: 154px;"><span class="thumb__photo thumb__photo--beet" role="img" aria-label="Bowl of heirloom beet salad"></span></div>
    <div class="thumb" style="top: 246px;"><span class="thumb__photo thumb__photo--cups" role="img" aria-label="Black bean and corn salad in lettuce cups"></span></div>
    <div class="thumb" style="top: 328px;"><span class="thumb__photo thumb__photo--mixed" role="img" aria-label="Bowl of green, red and white salad"></span></div>

    <div class="section-head section-head--toasts"><span class="section-head__title">Toasts</span><span class="section-head__rule"></span></div>

    <div class="dish" style="top: 500px;">
      <div class="dish__row"><span class="dish__bullet"></span><span class="dish__name">Everything Avocado toast</span><span class="dish__leader"></span><span class="dish__qty">QUANTITY</span><span class="dish__price">USD</span></div>
      <p class="dish__desc">Avocado on whole grain toast with<br>our signature spice blend</p>
    </div>
    <div class="dish" style="top: 581px;">
      <div class="dish__row"><span class="dish__bullet"></span><span class="dish__name">Tomato &amp; Beet Bruschetta</span><span class="dish__leader"></span><span class="dish__qty">QUANTITY</span><span class="dish__price">USD</span></div>
    </div>
    <div class="dish" style="top: 654px;">
      <div class="dish__row"><span class="dish__bullet"></span><span class="dish__name">Vegetable Melt on garlic Toast</span><span class="dish__leader"></span><span class="dish__qty">QUANTITY</span><span class="dish__price">USD</span></div>
    </div>

    <div class="thumb" style="top: 482px;"><span class="thumb__photo thumb__photo--avocado" role="img" aria-label="Avocado toast in a bowl"></span></div>
    <div class="thumb" style="top: 561px;"><span class="thumb__photo thumb__photo--bruschetta" role="img" aria-label="Tomato and beet bruschetta"></span></div>
    <div class="thumb" style="top: 639px;"><span class="thumb__photo thumb__photo--melt" role="img" aria-label="Vegetable melt on garlic toast"></span></div>
  </section>
</body>
</html>
```